依頼詳細
■ デザイン

期間限定のキャンペーンメニュー(縦)です。

印刷掲示・印刷物配布・HPで使用します。

ファスティング(断食)をするためのリゾートホテルの宿泊客へむけたキャンペーンです。

テーマは、健康、デトックス、ダイエット、美しくなる

メインターゲットは、健康志向が高い女性、30歳~60歳

文字は大きく(50歳代が裸眼で見えるサイズ)

■使用する場所
ホテル内フロント・アロマルームで印刷物にラミネートをかけて掲示します
客室インフォメーションブックで印刷物を掲示します
HPに掲載します

■ 納品ファイル
JPG ai PDF

■添付ファイル
キャンペーン企画書
イメージ画像(必ずしも本画像が必須というわけではありません。お手持ちなどがありましたらご提案ください。)

■デザイン納期
4月上旬予定

■画像
お手持ちのものなど、無償使用できる画像でご提案ください。
場合により弊社所有の画像への入れ替えを提案することがあります。

■最下段には、2パターン店舗情報を記入してください。

■詳しくは企画書をご覧ください。ご不明点はメールでお問い合わせください

記載項目
サイズ
A4
ページ数
片面
希望イメージ
シンプル 複雑
単色 カラフル
暗い 明るい
日常 高級
遊び心 厳粛
未来的 伝統的
女性的 男性的
納品ファイル
• 高解像度JPG (.jpg)
• イラストレーター形式 (.ai)
■ 選んだ理由

本キャンペーンのイメージと、メニューの両方がとてもわかりやすく表現されていました。
1、2つのメニューの見やすい色と配置。
2、年齢層高い方にも文字サイズがほどよい。
3、本企画のテーマが表現されている。
4、季節感が感じられる。
5、シンプルななかにも柑橘が香り立つように盛り込まれている。
などが決め手となりました。

■ 提案者全員のお礼・コメント

この度は弊社コンペに多数ご応募くださいましてありがとうございました。とても素晴らしい作品が多く選出にはとても苦労をしました。また引き続きよろしくお願いいたします。

```html
<!DOCTYPE html>
<html lang="ja">
<head>
<meta charset="UTF-8">
<title>爽健アロマデトックス</title>
<link href="https://fonts.googleapis.com/css2?family=Noto+Serif+JP:wght@400;500;700&family=Cormorant+Garamond:wght@500;600&display=swap" rel="stylesheet">
<style>
:root{
  --ink:#3a3330;
  --soft-ink:#6b625d;
  --pink:#d9908a;
  --mint:#eef3ea;
  --photo-a:#e9e2dc;
  --photo-b:#d7c9bf;
  --line:#e3b8b3;
}
*{margin:0;padding:0;box-sizing:border-box}
html,body{width:854px;height:1200px;overflow:hidden}
body{font-family:"Noto Serif JP",serif;color:var(--ink);background:var(--mint);position:relative}
.hero{position:absolute;left:0;top:0;width:854px;height:430px;
  background:linear-gradient(100deg,var(--photo-b) 0%,var(--photo-a) 45%,#f6f2ee 80%);}
.hero-fade{position:absolute;left:0;top:300px;width:854px;height:160px;
  background:linear-gradient(180deg,rgba(238,243,234,0),var(--mint) 80%)}
.tagline{position:absolute;writing-mode:vertical-rl;font-size:34px;line-height:40px;letter-spacing:5px;white-space:nowrap;color:var(--ink)}
.tagline.first{right:16px;top:20px}
.tagline.second{right:62px;top:105px}
.title{position:absolute;left:280px;top:345px;font-weight:700;font-size:82px;line-height:110px;letter-spacing:4px;white-space:nowrap}
.intro{position:absolute;left:0;width:854px;top:600px;text-align:center;font-size:16px;line-height:28px;color:var(--soft-ink)}
.head{position:absolute;top:680px;font-family:"Cormorant Garamond",serif;font-size:44px;color:var(--pink);letter-spacing:3px}
.head.menu{left:62px}.head.price{left:440px}
.item{position:absolute;left:62px;width:350px}
.item h3{font-size:22px;font-weight:500;margin-bottom:10px}
.item p{font-size:14px;line-height:24px;color:var(--soft-ink);padding-left:24px}
.item1{top:760px}.item2{top:905px}
.prices{position:absolute;left:440px;top:748px;font-size:21px;line-height:33px}
.prices div{display:flex;gap:22px;white-space:nowrap}
.prices .t{width:130px;text-align:right}
.note{position:absolute;left:470px;top:888px;font-size:12px;line-height:20px;color:var(--soft-ink)}
.info{position:absolute;left:440px;top:960px;width:330px;height:160px;border:1.5px solid var(--line);
  padding:16px 18px;font-size:14px;line-height:26px}
</style>
</head>
<body>
<div class="hero" role="img" aria-label="アロマトリートメントを受けてくつろぐ女性の写真"></div>
<div class="hero-fade"></div>
<div class="tagline first">エステを受けて、</div>
<div class="tagline second">より一層美しい身体へ。</div>
<h1 class="title">爽健アロマ<br>デトックス</h1>
<p class="intro">伊豆特産ダイダイとグレープフルーツオイルで滞った毒素を分解。<br>さらにリンパ活性トリートメントでデトックスをうながします。</p>

<div class="head menu">menu</div>
<div class="head price">price</div>

<div class="item item1">
  <h3>・利尿デトックスボディ</h3>
  <p>グレープフルーツオイルに含まれる<br>D-リモネン成分が、余分な水分の排出<br>をうながし、巡りを整えファスティング<br>をサポートします。</p>
</div>
<div class="item item2">
  <h3>・爽快デトックスボディ</h3>
  <p>伊豆ダイダイが副交感神経を刺激して<br>大腸を活性化。ペッパーやジンジャー<br>成分で溜め込んだデトックスをサポート<br>します。</p>
</div>

<div class="prices">
  <div><span class="t">おためし45分</span><span>¥ 6,300</span></div>
  <div><span class="t">60分</span><span>¥ 8,470</span></div>
  <div><span class="t">90分</span><span>¥12,540</span></div>
  <div><span class="t">120分</span><span>¥15,730</span></div>
</div>
<p class="note">前日までのご予約で ¥500 割引します<br>※60 分以上が対象です</p>

<div class="info">
  お問合せはフロントまで承ります<br>
  営業時間 15：00 ～ 22：00<br>
  受付時間 15：00 ～ 18：00<br>
  アロマルーム／館内 1 階にございます<br>
  （全コース男女とも施術できます）
</div>
</body>
</html>
```